Consulting company needs website design

We need a simple, static website design for our consulting company. We are looking for a general design of the look and feel of the website. Initially, it will have these pages:
- Home
- About us
- Services
- Contact us
We have our own logo which I have attached to the brief.

We are looking for a simple website, with white background and the use of gray (darker) as the main theme. Simple fonts. The website should be responsive so it an be easily red in mobile devices.

As part of the project, we will need to receive at least the following items:
- Individual files with sample text to support the pages outlined above
- Necessary CSS files

Our current website is here: http://www.lantrovale.co/

Here are some examples of other website we like to be used as guideline:
- http://www.morvicaplanos.com/
-

Target Market(s)

Individuals and companies looking to hire our company to provide consulting services.

Industry/Entity Type

It Company

Coding

Coded - Design and coding required

Number of Pages Required

4 page

Font styles to use
Sans Serif

Requirements
Must have
• Main page should have the ability to embed Chirplet feed into it.
• We prefer the design to use gray tones.

```html
<!DOCTYPE html>
<html lang="en">
<head>
<meta charset="utf-8">
<title>Lantrovale Group SAS</title>
<link href="https://fonts.googleapis.com/css2?family=Roboto:wght@400;500;700&family=Architects+Daughter&display=swap" rel="stylesheet">
<style>
:root{
  --header-bg:#f7f8f9;
  --ink:#2b2f33;
  --body-text:#6b7075;
  --soft-bg:#f1f3f5;
  --brand-blue:#0d4a6b;
  --hero-dark:#2f3e52;
  --band-navy:#1d3459;
  --footer-bg:#363b42;
  --footer-text:#a3a8ae;
  --footer-head:#ffffff;
  --placeholder:#b9bcc0;
  --white:#ffffff;
}
*{margin:0;padding:0;box-sizing:border-box}
html,body{width:1200px;height:2219px;overflow:hidden}
body{font-family:'Roboto',Arial,sans-serif;color:var(--ink);background:var(--white);position:relative}
.abs{position:absolute}

/* header */
.site-header{position:absolute;left:0;top:0;width:1200px;height:69px;background:var(--header-bg)}
.brand{position:absolute;left:66px;top:10px;display:flex;align-items:center;gap:10px}
.brand-mark{width:46px;height:46px;border-radius:50%;border:2px solid #9aa0a6}
.brand-name{font-size:14px;line-height:17px;color:#555b61;font-weight:400}
.main-nav{position:absolute;top:26px;left:0;width:1200px;font-size:12.5px;font-weight:500;color:#222}
.main-nav a{position:absolute;text-decoration:none;color:inherit;white-space:nowrap}

/* hero */
.hero{position:absolute;left:0;top:69px;width:1200px;height:489px;
  background:linear-gradient(100deg,#3c4a5e 0%,#56657a 45%,#8593a6 75%,#6f7b8b 100%)}
.hero-title{position:absolute;left:222px;top:50px;font-family:'Architects Daughter',cursive;font-size:70px;line-height:74px;color:var(--white);font-weight:400}
.hero-sub{position:absolute;left:225px;top:300px;font-size:19.5px;line-height:29px;color:var(--white);font-weight:500}
.btn{position:absolute;top:381px;height:31px;font-size:8.5px;font-weight:700;text-transform:uppercase;display:flex;align-items:center;justify-content:center;border-radius:2px}
.btn-primary{left:225px;width:90px;background:var(--white);color:var(--brand-blue)}
.btn-outline{left:346px;width:75px;border:1px solid var(--white);color:var(--white)}
.slider-dots{position:absolute;left:567px;top:457px;display:flex;gap:10px}
.slider-dots span{width:9px;height:9px;border-radius:50%;background:var(--white)}
.slider-dots span.hollow{background:transparent;border:1.5px solid var(--white)}

/* partners */
.partners{position:absolute;left:0;top:558px;width:1200px;height:352px;background:var(--soft-bg)}
.section-title{position:absolute;left:0;width:1200px;text-align:center;font-size:21px;font-weight:500;color:var(--ink)}
.dotted-rule{position:absolute;left:40px;width:1123px;border-top:1px dotted #c4c8cc}
.pillar{position:absolute;width:340px;text-align:center}
.pillar-icon{width:76px;height:82px;background:var(--brand-blue);margin:0 auto;display:flex;align-items:center;justify-content:center}
.pillar h3{font-size:17.5px;font-weight:500;margin-top:16px;color:var(--ink)}
.pillar p{font-size:12.5px;line-height:19.5px;color:var(--body-text);margin-top:16px}

/* band */
.vision-band{position:absolute;left:0;top:910px;width:1200px;height:274px;
  background:linear-gradient(90deg,#2a4670 0%,#1f3a64 40%,#17305a 70%,#122850 100%)}

/* services */
.services{position:absolute;left:0;top:1184px;width:1200px;height:474px;background:var(--white)}
.service{position:absolute;width:272px;text-align:center}
.service svg{display:block;margin:0 auto;width:44px;height:44px}
.service h3{font-size:17.5px;font-weight:500;margin-top:13px;color:var(--ink)}
.service p{font-size:12.3px;line-height:19px;color:var(--body-text);margin-top:14px}

/* partner strip */
.partner-strip{position:absolute;left:0;top:1658px;width:1200px;height:144px;background:var(--soft-bg)}
.partner-badge{position:absolute;top:54px;width:140px;height:34px;display:flex;align-items:center;gap:10px}
.partner-badge .dot{width:30px;height:30px;border-radius:50%;background:#c8ccd0}
.partner-badge .bar{flex:1;height:14px;border-radius:7px;background:#d3d6da}

/* footer */
.site-footer{position:absolute;left:0;top:1802px;width:1200px;height:417px;background:var(--footer-bg);color:var(--footer-text)}
.footer-col{position:absolute;top:52px;width:260px}
.footer-col h4{font-size:17.5px;font-weight:500;color:var(--footer-head);margin-bottom:20px}
.footer-col p{font-size:12.3px;line-height:19px}
.contact-line{margin-top:14px}
.contact-line b{font-weight:400;color:#d9dcdf}
.social{display:flex;gap:12px;margin-top:18px}
.social span{width:11px;height:11px;border-radius:50%;background:#8f959b}
.post{display:flex;gap:16px;align-items:center;margin-bottom:24px}
.thumb{width:47px;height:47px;border-radius:50%;background:var(--placeholder);color:#555;font-size:8px;display:flex;align-items:center;justify-content:center;flex-shrink:0}
.post-title{font-size:12.5px;color:#e6e8ea}
.post-meta{font-size:10.5px;color:#8f959b;margin-top:5px}
.quote{display:flex;gap:12px}
.quote-mark{font-size:50px;line-height:40px;color:#9aa0a6;font-family:Georgia,serif;font-weight:700}
.reviewer{display:flex;align-items:center;gap:16px;margin-top:26px}
.reviewer .avatar{width:94px;height:94px;border-radius:50%;background:var(--placeholder);color:#333;font-size:14px;display:flex;align-items:center;justify-content:center}
.reviewer .name{font-size:16px;color:#e6e8ea}
.reviewer .role{font-size:12px;color:#8f959b;margin-top:8px}
.footer-rule{position:absolute;left:52px;top:350px;width:1096px;border-top:1px solid #4a5057}
.copyright{position:absolute;left:52px;top:378px;font-size:12px;color:var(--footer-text)}
</style>
</head>
<body>

<header class="site-header">
  <div class="brand">
    <div class="brand-mark"></div>
    <div class="brand-name">Lantrovale<br>Group SAS</div>
  </div>
  <nav class="main-nav">
    <a style="left:426px">HOME</a>
    <a style="left:502px">ABOUT US</a>
    <a style="left:601px">SERVICES</a>
    <a style="left:700px">CONTACT US</a>
  </nav>
</header>

<section class="hero" role="img" aria-label="Photo of hands reviewing printed business charts beside a coffee cup">
  <h1 class="hero-title">Customer<br>Oriented<br>Culture</h1>
  <p class="hero-sub">We offer quantitative and qualitative<br>solutions tailored to our clients’ needs</p>
  <span class="btn btn-primary">Our Services</span>
  <span class="btn btn-outline">Our Work</span>
  <div class="slider-dots"><span></span><span></span><span class="hollow"></span><span></span></div>
</section>

<section class="partners">
  <h2 class="section-title" style="top:14px">Partners &amp; Consulting Analysis</h2>
  <div class="dotted-rule" style="top:47px"></div>

  <div class="pillar" style="left:55px;top:87px">
    <div class="pillar-icon">
      <svg width="42" height="42" viewBox="0 0 24 24" fill="none" stroke="#fff" stroke-width="1.3" stroke-linejoin="round"><path d="M3 10h4v10H3zM7 11l4-7c1.5 0 2 1 2 2l-1 4h6c1.2 0 2 1 1.8 2l-1.3 6c-.2 1-1 2-2 2H7"/></svg>
    </div>
    <h3>Who we are</h3>
    <p>The quality perception of the product, what clients would like to change, what price can they afford, where is this product wanted the most, what causes dissatisfaction in a product (i.e. price, quality,design)</p>
  </div>

  <div class="pillar" style="left:429px;top:87px">
    <div class="pillar-icon">
      <svg width="40" height="40" viewBox="0 0 24 24" fill="none" stroke="#fff" stroke-width="1.3" stroke-linejoin="round"><path d="M12 2c3 3 3.5 8 2.5 13h-5C8.5 10 9 5 12 2z"/><circle cx="12" cy="9" r="1.5"/><path d="M9.5 13l-2.5 3v2l3-1.5M14.5 13l2.5 3v2l-3-1.5M11 17.5l1 3 1-3"/></svg>
    </div>
    <h3>Our Mission</h3>
    <p>Lantrovale Group is a team of research professionals that work toward delivering research services while upholding the highest standards of design, analysis and reporting. Our mission is to help set the industry in consulting services</p>
  </div>

  <div class="pillar" style="left:804px;top:87px">
    <div class="pillar-icon">
      <svg width="40" height="40" viewBox="0 0 24 24" fill="none" stroke="#fff" stroke-width="1.3" stroke-linejoin="round"><path d="M6 2h9l4 4v16H6z"/><path d="M15 2v4h4M9 10h7M9 13h7M9 16h7"/></svg>
    </div>
    <h3>Our Vision</h3>
    <p>Our vision is to be a long-term preferred partner to our clients in the field of market research and business consulting. We are relentlessly focused on delivering exceptional value in provision of strategy, research and analysis</p>
  </div>
</section>

<section class="vision-band" role="img" aria-label="Chalk-style illustration over a world map showing management, vision and organization ideas with a rising bar chart"></section>

<section class="services">
  <h2 class="section-title" style="top:24px">What We Do</h2>
  <div class="dotted-rule" style="top:52px;left:52px;width:1096px"></div>

  <div class="service" style="left:42px;top:108px">
    <svg viewBox="0 0 24 24" fill="none" stroke="#222" stroke-width="1.1"><circle cx="12" cy="12" r="4"/><path d="M12 10v4M11 11h1.6a.8.8 0 010 1.6h-1.2a.8.8 0 000 1.6H13"/><circle cx="4" cy="4" r="2"/><circle cx="20" cy="4" r="2"/><circle cx="4" cy="20" r="2"/><circle cx="20" cy="20" r="2"/><path d="M5.5 5.5l3.5 3.5M18.5 5.5L15 9M5.5 18.5L9 15M18.5 18.5L15 15"/></svg>
    <h3>Business Strategy</h3>
    <p>Sed ut perspiciatis unde omnis iste natus error sit voluptate accusantium doloremqu.</p>
  </div>
  <div class="service" style="left:323px;top:108px">
    <svg viewBox="0 0 24 24" fill="none" stroke="#222" stroke-width="1.1"><circle cx="12" cy="8" r="4.5"/><path d="M3 22c0-5 4-8 9-8s9 3 9 8zM12 14l-1.5 3 1.5 5 1.5-5z"/></svg>
    <h3>Executive Coaching</h3>
    <p>Nemo qui enim ipsam voluptatem quia voluptas sit aspernatur aut odit aut fugit.</p>
  </div>
  <div class="service" style="left:604px;top:108px">
    <svg viewBox="0 0 24 24" fill="none" stroke="#222" stroke-width="1.1"><path d="M12 2v4M12 2h3v1.5h-3M4 10c2-3 5-4 8-4s6 1 8 4zM3 10h18M3 22h18M5 12v8M9 12v8M12 12v8M15 12v8M19 12v8"/></svg>
    <h3>Corporate Governance</h3>
    <p>Sed ut perspiciatis unde omnis iste natus error sit voluptatem accusantium quido et.</p>
  </div>
  <div class="service" style="left:885px;top:108px">
    <svg viewBox="0 0 24 24" fill="none" stroke="#222" stroke-width="1.1"><circle cx="12" cy="14" r="7.5"/><path d="M10 3h4M12 3v3.5M12 14l3-3"/></svg>
    <h3>Performance Management</h3>
    <p>Ut enim ad minim veniam, quis nostrud etor exercitation ullamco laboris nisi ut aliquipe.</p>
  </div>

  <div class="service" style="left:42px;top:306px">
    <svg viewBox="0 0 24 24" fill="none" stroke="#222" stroke-width="1.1"><path d="M7 17H6a4.5 4.5 0 010-9 6 6 0 0111.5 1A4 4 0 0118 17h-1M12 11v10M9 18l3 3 3-3"/></svg>
    <h3>Ethics and Compliance (E&amp;C)</h3>
    <p>Sed ut perspiciatis unde omnis iste natus error sit voluptate accusantium doloremqu.</p>
  </div>
  <div class="service" style="left:323px;top:306px">
    <svg viewBox="0 0 24 24" fill="none" stroke="#222" stroke-width="1.1"><path d="M12 1.5l2 2 2.8-.5.8 2.7 2.7.8-.5 2.8 2 2-2 2 .5 2.8-2.7.8-.8 2.7-2.8-.5-2 2-2-2-2.8.5-.8-2.7-2.7-.8.5-2.8-2-2 2-2-.5-2.8 2.7-.8.8-2.7 2.8.5z"/><text x="12" y="13.8" font-size="5" text-anchor="middle" fill="#222" stroke="none" font-family="Roboto,sans-serif">NEW</text></svg>
    <h3>New Business Development</h3>
    <p>Nemo qui enim ipsam voluptatem quia voluptas sit aspernatur aut odit aut fugit.</p>
  </div>
  <div class="service" style="left:604px;top:306px">
    <svg viewBox="0 0 24 24" fill="none" stroke="#222" stroke-width="1.1"><circle cx="9" cy="9" r="3"/><path d="M9 2v2M9 14v2M2 9h2M14 9h2M4 4l1.5 1.5M12.5 12.5L14 14M4 14l1.5-1.5M12.5 5.5L14 4"/><rect x="13" y="13" width="9" height="9"/><path d="M15 17.5l1.8 1.8L20 15.5"/></svg>
    <h3>Risk Management</h3>
    <p>Sed ut perspiciatis unde omnis iste natus error sit voluptatem accusantium quido et.</p>
  </div>
  <div class="service" style="left:885px;top:306px">
    <svg viewBox="0 0 24 24" fill="none" stroke="#222" stroke-width="1.1" stroke-linejoin="round"><path d="M12 2l3 6.5 7 .8-5.2 4.8 1.4 7L12 17.5 5.8 21l1.4-7L2 9.3l7-.8z"/></svg>
    <h3>Financial Management</h3>
    <p>Duis aute irure dolor in reprehenderit in ter voluptate velit esse cillum dolore eu fugiat.</p>
  </div>
</section>

<section class="partner-strip" aria-label="Partner badges">
  <div class="partner-badge" style="left:60px"><span class="dot"></span><span class="bar"></span></div>
  <div class="partner-badge" style="left:248px"><span class="dot"></span><span class="bar"></span></div>
  <div class="partner-badge" style="left:433px"><span class="dot"></span><span class="bar"></span></div>
  <div class="partner-badge" style="left:626px"><span class="dot"></span><span class="bar"></span></div>
  <div class="partner-badge" style="left:812px"><span class="dot"></span><span class="bar"></span></div>
  <div class="partner-badge" style="left:999px"><span class="dot"></span><span class="bar"></span></div>
</section>

<footer class="site-footer">
  <div class="footer-col" style="left:52px">
    <h4>Contact Us</h4>
    <p>Maecenas etos sit amet, consectetur adipiscing elit. Terminal volutpat rutrum metro amet sollicitudin interdum.</p>
    <p class="contact-line" style="margin-top:18px"><b>Phone:</b> +1 (800) 555 01 42</p>
    <p class="contact-line"><b>Office:</b> 4710 Alder Street, New York</p>
    <p class="contact-line"><b>Email:</b> info@lantrovale.co</p>
    <div class="social"><span></span><span></span><span></span><span></span><span></span></div>
  </div>

  <div class="footer-col" style="left:333px">
    <h4>Recent Posts</h4>
    <div class="post"><div class="thumb">50x50</div><div><div class="post-title">Business Cards Design Trends</div><div class="post-meta">Dec 02, 2020 / 2 comments</div></div></div>
    <div class="post"><div class="thumb">50x50</div><div><div class="post-title">This Maravelous App</div><div class="post-meta">Nov 18, 2020 / 9 comments</div></div></div>
    <div class="post"><div class="thumb">50x50</div><div><div class="post-title">Brand Paper Niceties</div><div class="post-meta">Nov 10, 2020 / 0 comments</div></div></div>
  </div>

  <div class="footer-col" style="left:614px">
    <h4>Latest Chirps</h4>
  </div>

  <div class="footer-col" style="left:895px">
    <h4>Last Review</h4>
    <div class="quote">
      <span class="quote-mark">“</span>
      <p>Lorem ipsum dolor sit amet, consectetur adipiscing elit, sed do eiusmod tempor incididunt ut labore et dolore magna aliqua. Ut enim ad minim veniam, quis nostrud exercitation ullamco.</p>
    </div>
    <div class="reviewer">
      <div class="avatar">84x84</div>
      <div><div class="name">Daniel Morrow</div><div class="role">Creative Designer</div></div>
    </div>
  </div>

  <div class="footer-rule"></div>
  <p class="copyright">Copyright 2020. All Rights Reserved by Lantrovale Group</p>
</footer>

</body>
</html>
```